Google Form Graphic to suit our Brand and industry

Create a graphic / image for us to put at the top of our client enquiry google form.
The image will be a section of an architectural home with our branding over the top. Preferably translucent.
The image must suit the shape of the google forms image, which is an elongated rectangle
#003d5d - brand colour

Target Market(s)

residential home owners, high end architectural homes

Industry/Entity Type

Residential construction

Colors
0054AA
0677BA
7BADD7
CADEEF
E8F1F8

Requirements
Must have
• our branding and a photo of an architectural home in the background

```html
<!DOCTYPE html>
<html lang="en">
<head>
<meta charset="utf-8">
<title>New Client Enquiry Form</title>
<link rel="stylesheet" href="https://fonts.googleapis.com/css2?family=Montserrat:wght@500&family=Roboto:wght@400&display=swap">
<style>
  :root {
    --page-bg: #ebeef2;
    --card-bg: #ffffff;
    --card-border: #dadce0;
    --accent-bar: #2b4c6b;
    --brand-navy: #133c5c;
    --text-main: #202124;
    --text-muted: #70757a;
    --required: #d93025;
    --rule: #9aa0a6;
    --brand-text: #ffffff;
  }
  * { box-sizing: border-box; margin: 0; padding: 0; }
  html, body {
    width: 1194px;
    height: 1200px;
    overflow: hidden;
    background: var(--page-bg);
    font-family: "Roboto", Arial, sans-serif;
    color: var(--text-main);
  }
  .form-page { position: relative; width: 1194px; height: 1200px; }

  .form-header {
    position: absolute;
    left: 21px; top: 18px;
    width: 1164px; height: 291px;
    border-radius: 12px;
    overflow: hidden;
  }
  .form-header svg { display: block; }
  .brand-name {
    font-family: "Montserrat", Arial, sans-serif;
    font-weight: 500;
    font-size: 34px;
    letter-spacing: 6px;
    fill: var(--brand-text);
  }

  .card {
    position: absolute;
    left: 21px;
    width: 1161px;
    background: var(--card-bg);
    border: 1.5px solid var(--card-border);
    border-radius: 12px;
  }
  .title-card {
    top: 328px; height: 206px;
    overflow: hidden;
  }
  .title-card::before {
    content: "";
    position: absolute; left: 0; top: 0; right: 0;
    height: 15px;
    background: var(--accent-bar);
  }
  .form-title {
    position: absolute; left: 36px; top: 52px;
    font-size: 48px; font-weight: 400;
    color: var(--text-main);
  }
  .form-description {
    position: absolute; left: 36px; top: 140px;
    font-size: 21px;
    color: var(--text-main);
  }

  .question-card.source { top: 556px; height: 206px; }
  .question-card.name { top: 783px; height: 204px; }
  .question-card.phone { top: 1008px; height: 230px; }

  .question-label {
    position: absolute; left: 36px; top: 38px;
    font-size: 24px;
  }
  .required-mark { color: var(--required); margin-left: 4px; }
  .answer-field {
    position: absolute; left: 36px; top: 105px;
    width: 543px;
    padding-bottom: 10px;
    border-bottom: 1.5px dotted var(--rule);
    font-size: 21px;
    color: var(--text-muted);
  }
</style>
</head>
<body>
<main class="form-page">
  <header class="form-header">
    <svg width="1164" height="291" viewBox="0 0 1164 291">
      <defs>
        <linearGradient id="home-photo-left" x1="0" y1="0" x2="0" y2="1">
          <stop offset="0" stop-color="#c9cdc9"/>
          <stop offset="0.45" stop-color="#a8967c"/>
          <stop offset="0.8" stop-color="#6f6a5c"/>
          <stop offset="1" stop-color="#8d9aa0"/>
        </linearGradient>
        <linearGradient id="home-photo-right" x1="0" y1="0" x2="1" y2="1">
          <stop offset="0" stop-color="#8fb0df"/>
          <stop offset="0.5" stop-color="#e4e6ea"/>
          <stop offset="1" stop-color="#c7c9cc"/>
        </linearGradient>
      </defs>
      <rect class="brand-band" x="0" y="0" width="1164" height="291" fill="var(--brand-navy)"/>
      <rect role="img" aria-label="Photo of a modern two-storey architectural home with glass walls at dusk" x="0" y="0" width="357" height="291" fill="url(#home-photo-left)"/>
      <rect role="img" aria-label="Photo of a white modern home facade with large framed windows against blue sky" x="780" y="0" width="384" height="291" fill="url(#home-photo-right)"/>
      <text class="brand-name" x="571" y="158" text-anchor="middle">VELA HOMES</text>
    </svg>
  </header>

  <section class="card title-card">
    <h1 class="form-title">New Client Enquiry Form</h1>
    <p class="form-description">We would love to hear your thought or feedback on how we can improve your experience !!</p>
  </section>

  <section class="card question-card source">
    <p class="question-label">Firstly, how did you hear about us ?<span class="required-mark">*</span></p>
    <div class="answer-field">Short answer text</div>
  </section>

  <section class="card question-card name">
    <p class="question-label">Name</p>
    <div class="answer-field">Short answer text</div>
  </section>

  <section class="card question-card phone">
    <p class="question-label">Phone</p>
    <div class="answer-field">Short answer text</div>
  </section>
</main>
</body>
</html>
```